Business IT Services Billboard to attract local small businesses

We are Brivolane, a premier Managed Service Provider (MSP) specializing in comprehensive IT services and VOIP phone solutions exclusively for businesses. Our goal is to create a dynamic and visually engaging billboard advertisement that not only highlights our cutting-edge IT solutions but also emphasizes our state-of-the-art VOIP phone services. This billboard should communicate our commitment to providing innovative, reliable, and holistic technology solutions.
Target Market(s)
small business
Industry/Entity Type
Information Technology
Colors
Designer to choose colors to be used in the design.
Look and feel
Each slider illustrates characteristics of the customer's brand and the style your logo design should communicate.

```html
<!DOCTYPE html>
<html lang="en">
<head>
<meta charset="utf-8">
<title>Brivolane Billboard</title>
<link rel="stylesheet" href="https://fonts.googleapis.com/css2?family=Poppins:wght@300;400;500;600;700;800&display=swap">
<style>
  :root{
    --page:#d6d6d6;
    --blue:#1a6fc0;
    --blue-bright:#12a8ea;
    --blue-deep:#0b3f7a;
    --navy:#081c3a;
    --cyan:#1ab8f2;
    --charcoal:#333436;
    --grey:#a9abae;
    --white:#ffffff;
    --ink:#1d1d1f;
  }
  *{margin:0;padding:0;box-sizing:border-box}
  html,body{width:918px;height:1200px;overflow:hidden}
  body{background:var(--page);font-family:"Poppins",sans-serif;position:relative}
  .billboard{
    position:absolute;left:29px;top:385px;width:860px;height:430px;
    overflow:hidden;box-shadow:0 14px 24px rgba(0,0,0,.35);background:var(--white);
  }
  .billboard__shapes{position:absolute;inset:0}
  .t{position:absolute;white-space:nowrap;line-height:1}
  .brand{left:32px;top:28px;font-size:40px;font-weight:800;color:var(--blue);letter-spacing:1px;text-transform:uppercase}
  .phone{left:516px;top:26px;display:flex;align-items:center;gap:10px;color:var(--white);font-weight:700;font-size:35px}
  .phone svg{width:28px;height:28px}
  .headline{color:var(--white)}
  .headline .sm{font-size:17px;font-weight:400}
  .headline .lt{font-size:31px;font-weight:300}
  .headline .bd{font-weight:700}
  .hl-1{left:34px;top:111px}
  .hl-2{left:70px;top:150px}
  .hl-2 .bd{font-size:36px}
  .hl-2 .sm{font-size:19px}
  .hl-3{left:42px;top:196px;font-size:38px}
  .hl-3 .bd{font-weight:700}
  .hl-3 .rg{font-weight:400}
  .tagline{left:22px;font-size:16.5px;color:var(--white)}
  .tagline .hi{color:var(--cyan);font-weight:700}
  .tagline .bd{font-weight:700}
  .tag-1{top:270px}
  .tag-2{top:295px}
  .cta{left:22px;top:349px;font-size:12.5px;color:var(--ink)}
  .cta .hi{color:var(--blue);font-weight:700}
  .web{left:22px;top:369px;display:flex;align-items:center;gap:7px;font-size:16px;color:var(--ink)}
  .web .hi{color:var(--blue);font-weight:700}
  .web svg{width:14px;height:14px}
  .deskphone{position:absolute;left:232px;top:334px;width:140px;height:78px}
</style>
</head>
<body>
<div class="billboard">
  <svg class="billboard__shapes" viewBox="0 0 860 430" width="860" height="430">
    <defs>
      <linearGradient id="topBlue" x1="0" y1="0" x2="1" y2="0">
        <stop offset="0" stop-color="#1b66b5"/><stop offset="1" stop-color="#13a6e8"/>
      </linearGradient>
      <linearGradient id="panelBlue" x1="0" y1="0" x2="1" y2="0">
        <stop offset="0" stop-color="#1b62b0"/><stop offset="1" stop-color="#12a9ea"/>
      </linearGradient>
      <radialGradient id="photoGlow" cx="0.72" cy="0.35" r="0.6">
        <stop offset="0" stop-color="#f0a67a"/>
        <stop offset="0.18" stop-color="#7a6a8a"/>
        <stop offset="0.5" stop-color="#1c4f86"/>
        <stop offset="1" stop-color="#0a2448"/>
      </radialGradient>
    </defs>
    <g role="img" aria-label="Photo of a hand holding a smartphone beneath a glowing network globe with floating technology icons">
      <polygon points="471,94 860,94 860,430 357,430" fill="url(#photoGlow)"/>
    </g>
    <polygon points="0,0 502,0 471,94 0,94" fill="var(--white)"/>
    <polygon points="0,0 30,0 0,90" fill="var(--grey)"/>
    <polygon points="502,0 860,0 860,94 471,94" fill="url(#topBlue)"/>
    <polygon points="0,94 471,94 417,254 0,254" fill="url(#panelBlue)"/>
    <polygon points="0,254 417,254 392,326 0,326" fill="var(--charcoal)"/>
    <polygon points="0,326 392,326 363,411 0,411" fill="var(--white)"/>
    <rect x="0" y="411" width="200" height="19" fill="var(--charcoal)"/>
    <polygon points="200,411 363,411 357,430 200,430" fill="var(--blue)"/>
    <polygon points="860,220 860,430 800,430" fill="var(--blue-bright)"/>
  </svg>

  <div class="t brand">Brivolane</div>

  <div class="t phone">
    <svg viewBox="0 0 24 24" fill="none" stroke="#fff" stroke-width="2.2" stroke-linecap="round" stroke-linejoin="round">
      <path d="M5 3h3l2 5-2.5 1.5a11 11 0 0 0 6 6L15 13l5 2v3a2 2 0 0 1-2 2A16 16 0 0 1 3 5a2 2 0 0 1 2-2z"/>
      <path d="M15 3a6 6 0 0 1 6 6M15 7a2 2 0 0 1 2 2"/>
    </svg>
    <span>(352) 555-0148</span>
  </div>

  <div class="t headline hl-1"><span class="sm">Elevate Your </span><span class="lt">Business</span></div>
  <div class="t headline hl-2"><span class="sm">with </span><span class="bd">Next-Gen IT</span><span class="sm"> and</span></div>
  <div class="t headline hl-3"><span class="bd">VOIP</span> <span class="rg">Services</span></div>

  <div class="t tagline tag-1"><span class="hi">Innovative IT</span> and <span class="hi">VOIP Solutions</span></div>
  <div class="t tagline tag-2">Tailored for Your <span class="bd">Business Success.</span></div>

  <div class="t cta">Transform Your <span class="hi">Tech Today at</span></div>
  <div class="t web">
    <svg viewBox="0 0 16 16" fill="none" stroke="#1a6fc0" stroke-width="1.3">
      <circle cx="8" cy="8" r="6.5"/><ellipse cx="8" cy="8" rx="3" ry="6.5"/><path d="M1.5 8h13M2.5 4.8h11M2.5 11.2h11"/>
    </svg>
    <span>www.<span class="hi">brivolane</span>.com</span>
  </div>

  <svg class="deskphone" viewBox="0 0 140 78" role="img" aria-label="Photo of a desk VOIP phone with colour screen">
    <defs>
      <linearGradient id="phoneTone" x1="0" y1="0" x2="1" y2="1">
        <stop offset="0" stop-color="#4a4d52"/><stop offset="1" stop-color="#1e2024"/>
      </linearGradient>
    </defs>
    <polygon points="22,10 110,2 132,74 8,78" fill="url(#phoneTone)"/>
  </svg>
</div>
</body>
</html>
```